Webdesign für Bau von Wohnanlagen aus Containermodulen
Zielgruppe
Wir bauen Wohnanlagen, Bürogebäude, Kindergärten, Schulen etc. aus einzelnen Containermodulen - übernehmen die Montage, Umbau und Versetzung, Reparaturen und Einlagerungen. Unsere Zielgruppe sind überwiegend Firmen und Kommunen. Der Text für die Homepage ist bereits fertig. Hier erhalten Sie weitere Informationen über unser Tätigkeitsfeld.
Aufgabenstellung
Die Farbe unseres Logos ist blau. Sie sollte sich natürlich in der Homepage minimal widerspiegeln, aber nicht dominieren. Bilder sollten nicht zu klein gehalten werden. Wir möchten dadurch zeigen, was möglich ist (z.B. Umsetzungen von ganzen Containeranlagen am Stück - hier haben wir eine Monopolstellung).

```html
<!DOCTYPE html>
<html lang="de">
<head>
<meta charset="utf-8">
<title>Falk Montagearbeiten – Leistungen</title>
<link rel="stylesheet" href="https://fonts.googleapis.com/css2?family=Open+Sans:wght@400;600;700&family=Roboto+Slab:wght@300&display=swap">
<style>
  :root{
    --blue:#13238f;
    --ink:#333333;
    --nav:#3a3a3a;
    --tab:#eeeeee;
    --footer:#626262;
    --white:#ffffff;
  }
  *{box-sizing:border-box;margin:0;padding:0}
  html,body{width:1175px;height:1200px;overflow:hidden;background:var(--white)}
  body{position:relative;font-family:"Open Sans",Arial,sans-serif;color:var(--ink)}
  .abs{position:absolute}

  .brand{left:228px;top:17px;width:166px;height:63px;display:flex;align-items:center;gap:8px}
  .brand-square{width:14px;height:14px;background:var(--blue)}
  .brand-name{font-weight:700;font-size:17px;line-height:1.1;color:var(--blue);letter-spacing:.5px}
  .tagline{left:412px;top:14px;font-family:"Roboto Slab",Georgia,serif;font-weight:300;font-size:16px;color:#444}
  .main-nav{left:505px;top:69px;width:450px;font-size:10px;letter-spacing:.2px;color:var(--nav)}
  .main-nav a{position:absolute;top:0;white-space:nowrap;text-decoration:none;color:inherit}
  .main-nav a.active{color:var(--blue);font-weight:700}

  .hero{left:0;top:91px;width:1175px;height:303px;background:linear-gradient(180deg,#f0f0f0 0%,#e7e3e2 40%,#d9d5d4 75%,#f2f2f2 100%)}

  .breadcrumb{left:229px;top:402px;font-size:9px;color:#333}
  .breadcrumb .root{letter-spacing:2px}
  .breadcrumb .sep{margin:0 4px}

  .side-nav{left:228px;top:449px;width:166px}
  .side-nav a{display:block;height:31px;margin-bottom:6px;padding-left:10px;line-height:31px;font-size:11px;font-weight:600;color:#222;background:var(--tab);text-decoration:none}
  .side-nav a.active{background:var(--blue);color:var(--white)}

  .content{left:412px;top:443px;width:535px}
  .content h1{font-weight:400;font-size:20px;color:var(--blue);line-height:26px}
  .content h2{font-weight:700;font-size:11px;color:var(--blue);margin-top:5px;margin-bottom:20px}
  .content p{font-size:11px;line-height:18.5px;margin-bottom:18.5px}

  .card{top:811px;width:166px}
  .card-title{height:24px;background:var(--blue);color:var(--white);font-size:11px;font-weight:600;text-align:center;line-height:24px}
  .card-media{position:relative;height:118px}
  .card-arrow{position:absolute;right:-3px;bottom:-3px;width:25px;height:25px;background:var(--blue);border:2px solid var(--white);display:flex;align-items:center;justify-content:center}
  .card-text{margin-top:14px;font-size:11px;line-height:18.5px}

  .slogan{left:228px;top:1089px;font-size:20px;line-height:25px;color:var(--blue)}

  .footer{left:0;top:1162px;width:1175px;height:38px;background:var(--footer);color:var(--white);font-size:9px;letter-spacing:2px;padding-left:228px;line-height:38px}
</style>
</head>
<body>
  <header>
    <div class="abs brand"><span class="brand-square"></span><span class="brand-name">FALK<br>MONTAGE</span></div>
    <div class="abs tagline">Ihr Partner für mobile Container</div>
    <nav class="abs main-nav">
      <a style="left:0">HOME</a>
      <a class="active" style="left:55px">LEISTUNGEN</a>
      <a style="left:142px">WIR ÜBER UNS</a>
      <a style="left:238px">REFERENZEN</a>
      <a style="left:324px">AKTUELLES</a>
      <a style="left:401px">KONTAKT</a>
    </nav>
  </header>

  <div class="abs hero" role="img" aria-label="Zweigeschossige Containeranlage mit Außentreppen"></div>

  <div class="abs breadcrumb"><span class="root">FALK MONTAGEARBEITEN</span><span class="sep">»</span>Leistungen</div>

  <nav class="abs side-nav">
    <a>MONTAGE</a>
    <a class="active">UMBAU UND VERSETZUNG</a>
    <a>REPARATUR</a>
    <a>EINLAGERUNG</a>
  </nav>

  <main class="abs content">
    <h1>Dienstleistung aus erster Hand</h1>
    <h2>Wir machen Wünsche wahr</h2>
    <p>Temporäre Raumlösungen zu realisieren – das ist unsere Leidenschaft. Wir montieren mobile Containeranlagen wie Büro- und Wohncontainer nach Maß. Perfekt geeignet sind die Objekte für Schulen, Kindergärten, Bürogebäude, Krankenhäuser, Schauräume oder Wohnunterkünfte. Dabei schaffen wir individuelle Gebäude in unterschiedlichsten Größen und Varianten.</p>
    <p>Wenn der Platz zu eng wird oder neue Anforderungen einen Umbau oder eine Reparatur erfordern, sind wir genau in unserem Element. Von der kleinsten Korrektur bis zum spektakulären Umbau – wir machen es möglich.</p>
    <p>Sollte der Standort verlagert werden – wir versetzen ganze Containerstädte und machen Ihre mobile „Zwischenlösung“ zu einem angenehmen Arbeitsumfeld.</p>
    <p>Sie suchen einen Platz zum Einlagern? Auch dafür haben wir die passende Lösung.<br>Sprechen Sie uns gerne darauf an.</p>
  </main>

  <section class="abs card" style="left:228px">
    <div class="card-title">MONTAGE</div>
    <div class="card-media" role="img" aria-label="Kran bei der Montage einer Containeranlage" style="background:linear-gradient(180deg,#cfdbe8 0%,#7d9a6a 45%,#555a5e 100%)">
      <span class="card-arrow"><svg width="10" height="10" viewBox="0 0 10 10"><path d="M1 1l4 4-4 4M5 1l4 4-4 4" fill="none" stroke="#fff" stroke-width="1.4"/></svg></span>
    </div>
    <p class="card-text">Ihr mobiles Wunschobjekt stellen wir aus Containermodulen zusammen und montieren es direkt vor Ort genau nach Maß.</p>
  </section>

  <section class="abs card" style="left:412px">
    <div class="card-title">UMBAU UND VERSETZUNG</div>
    <div class="card-media" role="img" aria-label="Am Kran hängende Containeranlage" style="background:linear-gradient(180deg,#8fb3dc 0%,#c7d8ea 60%,#8a8d92 100%)">
      <span class="card-arrow"><svg width="10" height="10" viewBox="0 0 10 10"><path d="M1 1l4 4-4 4M5 1l4 4-4 4" fill="none" stroke="#fff" stroke-width="1.4"/></svg></span>
    </div>
    <p class="card-text">Egal, ob Sie nur einen kleinen Umbau planen oder<br>Ihr Containerbau an einen neuen Standort wechseln soll – wir kümmern uns um alles!</p>
  </section>

  <section class="abs card" style="left:597px">
    <div class="card-title">REPERATUR</div>
    <div class="card-media" role="img" aria-label="Innenraum mit geöffneter Deckenverkleidung" style="background:linear-gradient(180deg,#e4e4e2 0%,#f2f2ef 55%,#d8d2b8 100%)">
      <span class="card-arrow"><svg width="10" height="10" viewBox="0 0 10 10"><path d="M1 1l4 4-4 4M5 1l4 4-4 4" fill="none" stroke="#fff" stroke-width="1.4"/></svg></span>
    </div>
    <p class="card-text">Ist etwas defekt, reparieren wir selbstverständlich Ihr Bauobjekt – kostenbewusst und mit dem nötigen Know-how!</p>
  </section>

  <section class="abs card" style="left:782px">
    <div class="card-title">EINLAGERUNG</div>
    <div class="card-media" role="img" aria-label="Graue Containeranlage auf einem Lagerplatz" style="background:linear-gradient(180deg,#e6eaef 0%,#a9afb6 55%,#b7b1a5 100%)">
      <span class="card-arrow"><svg width="10" height="10" viewBox="0 0 10 10"><path d="M1 1l4 4-4 4M5 1l4 4-4 4" fill="none" stroke="#fff" stroke-width="1.4"/></svg></span>
    </div>
    <p class="card-text">Ihr Container kommt gerade nicht zum Einsatz? Dann darf er sich in unserem Zwischenlager ausruhen.</p>
  </section>

  <div class="abs slogan">Wir schaffen mobilen Raum.<br>Profitieren Sie von unserer langjährigen Erfahrung!</div>

  <footer class="abs footer">FALK MONTAGEARBEITEN &nbsp;| © 2017 &nbsp;| &nbsp;IMPRESSUM</footer>
</body>
</html>
```